Folder, biz cards, stationary, mailing labels, and labels containing my logo
Initiative KORVATH an engineering educational non-profit organization
Cutting-Edge
Marcus Tellfair
Executive Director
mtellfair@initiativekorvath-demo.org
www.initiativekorvath-demo.org
I will need a total of 6 business cards made.
we have a secondary logo that could be placed nicely on the back.
IK Main Logo
secondary logo that can be used on some documents

```html
<!DOCTYPE html>
<html lang="en">
<head>
<meta charset="utf-8">
<title>Initiative KORVATH — Stationery Set</title>
<link href="https://fonts.googleapis.com/css2?family=Montserrat:wght@400;600;700&display=swap" rel="stylesheet">
<style>
:root{
  --navy:#15307a;
  --blue:#2c5bc0;
  --sky:#6f93dd;
  --paper:#ffffff;
  --stage:#ebe8e3;
  --grey:#c9ccd3;
  --ink:#3a3f4b;
  --faint:#e6e9f0;
}
*{box-sizing:border-box;margin:0;padding:0}
html,body{width:1200px;height:394px;overflow:hidden;background:var(--stage);font-family:'Montserrat',sans-serif;color:var(--ink)}
.set{position:relative;width:1200px;height:394px}
.sheet{position:absolute;background:var(--paper);box-shadow:0 2px 6px rgba(0,0,0,.18);overflow:hidden}
.brand{font-weight:700;color:var(--navy);display:flex;align-items:center;gap:5px;white-space:nowrap;line-height:1}
.brand .dot{width:10px;height:10px;border-radius:50%;background:var(--blue);flex:none}
.brand.stack .name{line-height:1.05}
.brand.light{color:#fff}
.brand.light .dot{background:#fff}
.faint-circle{position:absolute;border-radius:50%;background:var(--faint)}
.wave{position:absolute;left:0;bottom:0;width:100%}

/* folder */
.folder-cover{left:12px;top:19px;width:156px;height:360px;background:linear-gradient(160deg,var(--sky) 0%,var(--blue) 45%,var(--navy) 100%)}
.folder-cover .faint-circle{left:38px;top:115px;width:80px;height:80px;background:rgba(255,255,255,.18)}
.folder-cover .spine{position:absolute;left:0;bottom:0;width:100%;height:95px;background:linear-gradient(180deg,#d8dbe1,#9aa0ab)}
.folder-cover .spine .brand{position:absolute;left:50%;bottom:18px;transform:translateX(-50%);font-size:7px}
.folder-inside{left:168px;top:19px;width:156px;height:360px}
.folder-inside > .brand{position:absolute;left:14px;top:22px;font-size:11px}
.folder-inside .faint-circle{left:38px;top:110px;width:80px;height:80px}
.folder-inside .pocket{position:absolute;left:0;bottom:0;width:100%;height:95px;background:linear-gradient(180deg,#eceef2,#b9bec8)}
.folder-inside .card-slot{position:absolute;left:40px;bottom:34px;width:76px;height:38px;background:var(--navy);display:flex;align-items:center;justify-content:center}
.folder-inside .card-slot .brand{font-size:6px}

/* letterhead */
.letterhead{left:384px;top:19px;width:192px;height:360px}
.letterhead .brand{position:absolute;left:14px;top:14px;font-size:10px}
.contact{position:absolute;right:8px;top:16px;font-size:3.8px;line-height:6.5px;color:var(--ink);text-align:left}
.letterhead .faint-circle{left:56px;top:110px;width:80px;height:80px}

/* fax */
.fax{left:600px;top:19px;width:192px;height:360px}
.fax .brand{position:absolute;left:14px;top:14px;font-size:10px}
.fax-title{position:absolute;left:14px;top:64px;font-size:15px;font-weight:700;color:var(--ink);letter-spacing:.5px}
.fax-fields{position:absolute;left:14px;top:86px;width:164px;display:grid;grid-template-columns:1fr 1fr;column-gap:10px;row-gap:5px}
.field{font-size:5px;border-bottom:.6px solid #888;padding-bottom:2px}
.checks{position:absolute;left:14px;top:150px;width:164px;display:flex;justify-content:space-between;font-size:3.6px}
.checks span{display:flex;align-items:center;gap:2px}
.checks i{width:4px;height:4px;border:.5px solid #666;display:inline-block}

/* envelopes */
.envelope-back{left:830px;top:24px;width:350px;height:120px;background:#f6f7f9}
.envelope-back svg{position:absolute;left:0;top:0}
.envelope-back .brand{position:absolute;left:155px;top:20px;font-size:6px}
.envelope{left:820px;top:120px;width:370px;height:160px}
.envelope .brand{position:absolute;left:18px;top:16px;font-size:11px}
.return{position:absolute;left:18px;top:48px;font-size:4.5px;line-height:7px}

/* business cards */
.card{width:100px;height:42px}
.card-front{left:880px;top:292px}
.card-front .brand{position:absolute;left:6px;top:6px;font-size:5.5px;gap:3px}
.card-front .brand .dot{width:7px;height:7px}
.card-front .who{position:absolute;right:6px;top:7px;text-align:right;font-size:3.4px;line-height:5px}
.card-front .who b{font-size:4.2px;color:var(--navy)}
.card-back{left:880px;top:342px;background:var(--navy);display:flex;align-items:center;justify-content:center}
.card-back .brand{font-size:6px}
.card-info{left:1000px;top:292px}
.card-info .who{position:absolute;left:7px;top:7px;font-size:3.6px;line-height:5.3px}
.card-info .who b{font-size:4.4px;color:var(--navy)}
</style>
</head>
<body>
<main class="set">

  <section class="sheet folder-cover" aria-label="Folder cover">
    <div class="faint-circle"></div>
    <div class="spine"><div class="brand light"><span class="dot"></span>Initiative KORVATH</div></div>
  </section>

  <section class="sheet folder-inside" aria-label="Folder inside">
    <div class="brand"><span class="dot"></span>Initiative KORVATH</div>
    <div class="faint-circle"></div>
    <div class="pocket">
      <div class="card-slot"><div class="brand light">Initiative KORVATH</div></div>
    </div>
  </section>

  <section class="sheet letterhead" aria-label="Letterhead">
    <div class="brand stack"><span class="dot"></span><span class="name">Initiative<br>KORVATH</span></div>
    <div class="contact">+1 555 014 2290<br>mtellfair@initiativekorvath-demo.org<br>www.initiativekorvath-demo.org</div>
    <div class="faint-circle"></div>
    <svg class="wave" viewBox="0 0 192 40" height="40" preserveAspectRatio="none">
      <path d="M0 22 C60 6 120 36 192 12 L192 40 L0 40Z" fill="var(--navy)"/>
      <path d="M0 18 C60 2 120 30 192 8" fill="none" stroke="var(--sky)" stroke-width="1.5"/>
    </svg>
  </section>

  <section class="sheet fax" aria-label="Fax sheet">
    <div class="brand stack"><span class="dot"></span><span class="name">Initiative<br>KORVATH</span></div>
    <div class="fax-title">FAX</div>
    <div class="fax-fields">
      <div class="field">To:</div><div class="field">From:</div>
      <div class="field">Fax:</div><div class="field">Pages:</div>
      <div class="field">Phone:</div><div class="field">Date:</div>
      <div class="field">Re:</div><div class="field">CC:</div>
    </div>
    <div class="checks">
      <span><i></i>Urgent</span><span><i></i>For Review</span><span><i></i>Please Comment</span><span><i></i>Please Reply</span><span><i></i>Please Recycle</span>
    </div>
    <svg class="wave" viewBox="0 0 192 40" height="40" preserveAspectRatio="none">
      <path d="M0 22 C60 6 120 36 192 12 L192 40 L0 40Z" fill="var(--navy)"/>
      <path d="M0 18 C60 2 120 30 192 8" fill="none" stroke="var(--sky)" stroke-width="1.5"/>
    </svg>
  </section>

  <section class="sheet envelope-back" aria-label="Envelope back">
    <svg width="350" height="120" viewBox="0 0 350 120">
      <path d="M0 0 L175 70 L350 0" fill="#eef0f4" stroke="#d3d7de"/>
      <path d="M0 95 C120 70 220 120 350 85 L350 120 L0 120Z" fill="var(--navy)"/>
    </svg>
    <div class="brand"><span class="dot"></span>Initiative KORVATH</div>
  </section>

  <section class="sheet envelope" aria-label="Envelope front">
    <div class="brand stack"><span class="dot"></span><span class="name">Initiative<br>KORVATH</span></div>
    <div class="return">48 Harbor Lane, Denver CO<br>www.initiativekorvath-demo.org</div>
    <svg class="wave" viewBox="0 0 370 50" height="50" preserveAspectRatio="none">
      <path d="M0 28 C120 4 240 48 370 14 L370 50 L0 50Z" fill="var(--navy)"/>
      <path d="M0 22 C120 -2 240 40 370 8" fill="none" stroke="var(--sky)" stroke-width="2"/>
    </svg>
  </section>

  <section class="sheet card card-front" aria-label="Business card front">
    <div class="brand stack"><span class="dot"></span><span class="name">Initiative<br>KORVATH</span></div>
    <div class="who"><b>Marcus Tellfair</b><br>Executive Director</div>
    <svg class="wave" viewBox="0 0 100 10" height="10" preserveAspectRatio="none">
      <path d="M0 6 C30 0 70 10 100 3 L100 10 L0 10Z" fill="var(--navy)"/>
    </svg>
  </section>

  <section class="sheet card card-info" aria-label="Business card contact side">
    <div class="who"><b>Marcus Tellfair</b><br>Executive Director<br>mtellfair@initiativekorvath-demo.org<br>www.initiativekorvath-demo.org</div>
    <svg class="wave" viewBox="0 0 100 10" height="10" preserveAspectRatio="none">
      <path d="M0 6 C30 0 70 10 100 3 L100 10 L0 10Z" fill="var(--navy)"/>
    </svg>
  </section>

  <section class="sheet card card-back" aria-label="Business card back">
    <div class="brand light"><span class="dot"></span>Initiative KORVATH</div>
  </section>

</main>
</body>
</html>
```